Digital Billboard Design: Winter Sales Event

I own a boutique furniture store in Calgary, AB (maplewoven.ca) and I am looking to advertise our winter sale event on a new curved digital billboard (specs attached including required file type).

I have this billboard rented for 52-weeks so I will be looking to change the design every 4-weeks (i.e. this is intended to be an ongoing project).

The objective of this first billboard is to raise awareness around our annual winter sales event. The store itself is only a few blocks from the billboard so those commuting into downtown are just a short drive from the store.

I am looking for a fresh, clean, contemporary look that will grab your attention as you drive into downtown Calgary without presenting to much info so as to be distracting (and overwhelming -- the billboard does not need to contain all info on my current marketing material). I should also note that the store caters to a higher-end, more sophisticated clientele so the graphics need to reflect the brand (i.e. we are not Brenton Furniture or Couch Depot!).

I have attached three files:

Billboard specs
Current marketing material advertising sale (and all relevant data)
An idea that is from an American furniture store that I think is interesting

Target Market(s)

Upper middle class, sophisticated client who appreciates the finer things in life.

Industry/Entity Type

Furniture Store

Font styles to use
Sans Serif

Requirements
Must have
• Company Logo
• Winter Sales Event - 20 to 60% off
• Address: 3847 22nd Ave SW
Nice to have
• Image of furniture -- see our website www.maplewoven.ca -- any photo from this site can be used
Should not have
• Too much text or visual distration

```html
<!DOCTYPE html>
<html lang="en">
<head>
<meta charset="utf-8">
<title>Maple Woven – Winter Sales Event Billboard</title>
<link rel="stylesheet" href="https://fonts.googleapis.com/css2?family=Source+Sans+3:wght@400;700&display=swap">
<style>
  :root {
    --stage: #2b2b2b;
    --sale-red: #ec1c24;
    --snow-white: #ffffff;
    --snow-tint: #f6a9ac;
  }
  * { margin: 0; padding: 0; box-sizing: border-box; }
  html, body {
    width: 1200px;
    height: 692px;
    overflow: hidden;
    background: var(--stage);
  }
  .billboard {
    position: absolute;
    left: 12px;
    top: 57px;
    width: 1176px;
    height: 516px;
    background: var(--sale-red);
    overflow: hidden;
  }
  .snowflake-frame {
    position: absolute;
    inset: 0;
    background:
      radial-gradient(ellipse 62% 52% at 50% 52%, var(--sale-red) 58%, rgba(236,28,36,0) 100%),
      linear-gradient(180deg, var(--snow-tint) 0%, var(--sale-red) 30%, var(--sale-red) 70%, var(--snow-tint) 100%);
  }
  .offer-card {
    position: absolute;
    left: 234px;
    top: 108px;
    width: 740px;
    height: 323px;
    background: var(--snow-white);
  }
  .offer-card::before {
    content: "";
    position: absolute;
    inset: 7px;
    border: 2px solid var(--sale-red);
    pointer-events: none;
  }
  .event-title {
    position: absolute;
    left: 0;
    right: 0;
    top: 14px;
    text-align: center;
    font-family: "Source Sans 3", sans-serif;
    font-weight: 700;
    font-size: 54px;
    color: var(--sale-red);
    line-height: 1;
  }
  .title-rule {
    position: absolute;
    left: 110px;
    width: 528px;
    top: 73px;
    height: 2px;
    background: var(--sale-red);
  }
  .discount {
    position: absolute;
    left: 0;
    right: 0;
    top: 98px;
    display: flex;
    justify-content: center;
    align-items: center;
    gap: 30px;
    font-family: "Source Sans 3", sans-serif;
    font-weight: 400;
    font-size: 46px;
    color: var(--sale-red);
    line-height: 1;
  }
  .discount svg { width: 30px; height: 30px; fill: var(--sale-red); }
  .brand-line {
    position: absolute;
    left: 10px;
    width: 716px;
    top: 183px;
    height: 66px;
    display: flex;
    align-items: center;
    justify-content: center;
  }
  .brand-name {
    font-family: "Source Sans 3", sans-serif;
    font-weight: 700;
    font-size: 56px;
    color: var(--sale-red);
    line-height: 1;
  }
  .store-address {
    position: absolute;
    left: 0;
    right: 0;
    top: 258px;
    text-align: center;
    font-family: "Source Sans 3", sans-serif;
    font-weight: 400;
    font-size: 44px;
    color: var(--sale-red);
    line-height: 1;
  }
</style>
</head>
<body>
  <main class="billboard">
    <div class="snowflake-frame" role="img" aria-label="White snowflake pattern framing the red banner"></div>
    <section class="offer-card">
      <h1 class="event-title">Winter Sales Event</h1>
      <div class="title-rule"></div>
      <p class="discount">
        <svg viewBox="0 0 24 24" aria-hidden="true"><polygon points="12,1 15,9 23.5,9 16.5,14 19,22.5 12,17.3 5,22.5 7.5,14 0.5,9 9,9"/></svg>
        <span>20 to 60% off</span>
        <svg viewBox="0 0 24 24" aria-hidden="true"><polygon points="12,1 15,9 23.5,9 16.5,14 19,22.5 12,17.3 5,22.5 7.5,14 0.5,9 9,9"/></svg>
      </p>
      <div class="brand-line">
        <span class="brand-name">Maple Woven</span>
      </div>
      <p class="store-address">3847 22ND AVE SW, CALGARY, AB</p>
    </section>
  </main>
</body>
</html>
```